Velvet Oaks rebranding my business with a new business card

I have my new logo and now I need a refresher on my business cards. I really want something fun and fresh. I like black background or anything to make the color pop.
Logo
Name: Velvet Oaks
Contact Info as stated below:
Mira Calloway
647-382-9164
Logo
Name: Velvet Oaks
Mira Calloway
647-382-9164
fb.me/VelvetOaksbyMira
Instagram: @VelvetOaksbyMira

Industry/Entity Type

Business

Contact Information for Business Card

double-sided. Logo on one side. Contact info on the other.

Requirements
Must have
• Logo
• Name: Velvet Oaks
• Contact Info as stated below:
• Mira Calloway
• 647-382-9164
• fb.me/VelvetOaksbyMira
• fb.me/VelvetOaksbyMira

```html
<!DOCTYPE html>
<html lang="en">
<head>
<meta charset="utf-8">
<title>Velvet Oaks – Business Card</title>
<link rel="stylesheet" href="https://fonts.googleapis.com/css2?family=Open+Sans:wght@400;600;700&display=swap">
<style>
  :root {
    --backdrop: #2b2b2d;
    --card: #111112;
    --card-panel: #19191b;
    --card-edge: #1f1f21;
    --accent-pink: #ec7fc0;
    --accent-teal: #4fc3b8;
    --text-light: #e2e2e2;
  }
  html, body {
    margin: 0;
    padding: 0;
    width: 1200px;
    height: 900px;
    overflow: hidden;
    background: var(--backdrop);
    font-family: "Open Sans", Arial, sans-serif;
  }
  .canvas {
    position: relative;
    width: 1200px;
    height: 900px;
  }
  .card {
    position: absolute;
    top: 300px;
    width: 525px;
    height: 300px;
    background: var(--card);
    border: 1px solid var(--card-edge);
    border-radius: 22px;
    box-shadow: 0 12px 32px rgba(0,0,0,.5);
    overflow: hidden;
  }
  .card--front { left: 50px; }
  .card--back { left: 625px; }

  .contact-panel {
    position: absolute;
    left: 272px;
    top: 0;
    right: 0;
    bottom: 0;
    background: var(--card-panel);
    border-left: 1px solid #232325;
  }

  .brand-mark {
    position: absolute;
    display: flex;
    align-items: center;
    color: var(--accent-pink);
    font-weight: 700;
    white-space: nowrap;
  }
  .brand-mark__dot {
    border-radius: 50%;
    background: var(--accent-teal);
    flex: none;
  }
  .card--front .brand-mark {
    left: 28px;
    top: 50%;
    transform: translateY(-50%);
    gap: 12px;
    font-size: 28px;
  }
  .card--front .brand-mark__dot { width: 58px; height: 58px; }
  .card--back .brand-mark {
    left: 50%;
    top: 50%;
    transform: translate(-50%, -50%);
    gap: 18px;
    font-size: 40px;
  }
  .card--back .brand-mark__dot { width: 86px; height: 86px; }

  .contact {
    position: absolute;
    left: 300px;
    top: 88px;
  }
  .contact__name {
    margin: 0 0 14px;
    color: var(--accent-pink);
    font-weight: 600;
    font-size: 22px;
  }
  .contact__list {
    list-style: none;
    margin: 0;
    padding: 0;
  }
  .contact__item {
    display: flex;
    align-items: center;
    gap: 10px;
    color: var(--text-light);
    font-size: 15px;
    line-height: 25px;
  }
  .contact__icon {
    width: 12px;
    height: 12px;
    flex: none;
    fill: var(--accent-pink);
  }
</style>
</head>
<body>
<main class="canvas">
  <section class="card card--front" aria-label="Business card, contact side">
    <div class="contact-panel"></div>
    <div class="brand-mark"><span class="brand-mark__dot"></span>Velvet Oaks</div>
    <div class="contact">
      <h1 class="contact__name">Mira Calloway</h1>
      <ul class="contact__list">
        <li class="contact__item">
          <svg class="contact__icon" viewBox="0 0 12 12" aria-hidden="true"><path d="M2.5 0.8 4.3 3.2 3.3 4.4c.7 1.6 2.1 3 3.8 3.8l1.2-1 2.4 1.8-1.2 2.2C5 10.8 1 6.8.6 2z"/></svg>
          647-382-9164
        </li>
        <li class="contact__item">
          <svg class="contact__icon" viewBox="0 0 12 12" aria-hidden="true"><path d="M0 2h12v8H0z"/><path d="M0.8 2.6 6 6.6l5.2-4" fill="none" stroke="#19191b" stroke-width="1"/></svg>
          hello@velvetoaks.ca
        </li>
        <li class="contact__item">
          <svg class="contact__icon" viewBox="0 0 12 12" aria-hidden="true"><circle cx="6" cy="6" r="5.5"/><path d="M1 6h10M6 .8c-2 3-2 7.4 0 10.4M6 .8c2 3 2 7.4 0 10.4" fill="none" stroke="#19191b" stroke-width=".9"/></svg>
          www.velvetoaks.ca
        </li>
        <li class="contact__item">
          <svg class="contact__icon" viewBox="0 0 12 12" aria-hidden="true"><rect x="1" y="1" width="10" height="10" rx="1.5"/></svg>
          fb.me/VelvetOaksbyMira
        </li>
      </ul>
    </div>
  </section>

  <section class="card card--back" aria-label="Business card, logo side">
    <div class="brand-mark"><span class="brand-mark__dot"></span>Velvet Oaks</div>
  </section>
</main>
</body>
</html>
```